Dale Morrikan Plumbing and Heating

Need a card design for a plumbing and heating company that does service and repair, remodels, and plumbing in new construction. Please add following on back side of card; Boilers, Water heaters, Gas lines, Sump pumps, Toilet repairs, Faucet repairs, Pipe thawing, Radiant heating, New construction, Remodels.

Industry/Entity Type

Plumber

Contact Information for Business Card

Was thinking white gloss card with colored logo in middle or black glossy card with silver logo in middle. Just a thought but very open to other designs.

Requirements
Must have
• Need following on front of card;
• P(203) 321-8689
• C(203) 232-9069
• Dale Morrikan 275 Larkwell St West, Stamford, Ct 06214
• service@DrainHearth.example (plumbing in blue, heating in red)
• www.DrainHearth.example (plumbing in blue, heating in red)
• Fully Licensed and Insured
Nice to have
• Elegant design

```html
<!DOCTYPE html>
<html lang="en">
<head>
<meta charset="utf-8">
<title>Dale Morrikan Plumbing and Heating – Business Card</title>
<link href="https://fonts.googleapis.com/css2?family=Lato:wght@400;700;900&display=swap" rel="stylesheet">
<style>
  :root {
    --bg: #8d8d8d;
    --paper: #f1f1f1;
    --grid: #e2e2e2;
    --ink: #1f1f1f;
    --panel: #232323;
    --panel-band: #141414;
    --blue: #1fa3dc;
    --blue-deep: #0f7fb4;
    --blue-light: #5cc4f0;
    --brand-blue: #2d3f9e;
    --brand-red: #b32025;
    --white: #ffffff;
  }
  * { box-sizing: border-box; margin: 0; padding: 0; }
  html, body { width: 1200px; height: 900px; overflow: hidden; }
  body {
    background: var(--bg);
    font-family: "Lato", sans-serif;
    position: relative;
  }
  .card {
    position: absolute;
    width: 640px;
    height: 366px;
    left: 280px;
    background-color: var(--paper);
    background-image:
      linear-gradient(var(--grid) 1px, transparent 1px),
      linear-gradient(90deg, var(--grid) 1px, transparent 1px);
    background-size: 22px 22px;
    overflow: hidden;
    box-shadow: 0 6px 18px rgba(0,0,0,.3);
  }
  .card--front { top: 48px; }
  .card--back { top: 486px; }

  /* front */
  .front-edge { position: absolute; left: 0; width: 18px; }
  .front-edge--blue { top: 0; height: 160px; background: var(--blue); }
  .front-edge--dark { top: 160px; bottom: 0; background: var(--panel); }
  .front-brand {
    position: absolute; left: 40px; top: 160px; width: 250px;
    text-align: center; color: var(--brand-blue);
    font-weight: 900; font-size: 19px; line-height: 1.2; text-transform: uppercase;
  }
  .front-brand small { display: block; font-size: 12px; letter-spacing: 2px; font-weight: 900; }
  .contact-panel { position: absolute; inset: 0; }
  .name-bar {
    position: absolute; left: 250px; top: 34px; width: 390px; height: 44px;
    background: var(--blue); color: var(--white);
  }
  .name-bar .name { position: absolute; left: 100px; top: 6px; font-weight: 900; font-size: 17px; text-transform: uppercase; }
  .name-bar .role { position: absolute; right: 50px; top: 26px; font-weight: 900; font-size: 9px; text-transform: uppercase; }
  .hex { position: absolute; width: 34px; height: 34px; }
  .contact-row {
    position: absolute; left: 345px; color: var(--white);
    font-size: 15px; line-height: 1.3;
  }
  .contact-row .drain { color: #4a63d8; }
  .contact-row .hearth { color: #d5343a; }

  /* back */
  .back-edge { position: absolute; top: 0; bottom: 0; }
  .back-edge--black-l { left: 0; width: 14px; background: var(--panel); }
  .back-edge--deep-l { left: 14px; width: 12px; background: var(--blue-deep); }
  .back-edge--blue-l { left: 26px; width: 14px; background: var(--blue); }
  .back-edge--light-r { right: 52px; width: 22px; background: var(--blue-light); }
  .back-edge--blue-r { right: 30px; width: 22px; background: var(--blue); }
  .back-edge--black-r { right: 0; width: 30px; background: var(--panel); }
  .licence {
    position: absolute; right: 52px; bottom: 18px; width: 22px;
    writing-mode: vertical-rl; transform: rotate(180deg);
    display: flex; align-items: center; justify-content: flex-start;
    font-size: 13px; font-weight: 700; color: var(--ink); white-space: nowrap;
    line-height: 22px;
  }
  .back-content { position: absolute; left: 60px; right: 100px; top: 34px; text-align: center; }
  .back-brand {
    color: var(--brand-blue); font-weight: 900; font-size: 32px;
    text-transform: uppercase; line-height: 1.1;
  }
  .back-brand small { display: block; font-size: 19px; letter-spacing: 4px; }
  .tagline {
    margin-top: 16px; color: var(--brand-red); font-weight: 700;
    font-size: 13px; font-variant: small-caps; letter-spacing: .3px;
  }
  .services { margin-top: 8px; color: var(--brand-blue); font-size: 16px; line-height: 1.3; }
  .back-url { margin-top: 12px; font-size: 22px; letter-spacing: 1px; color: var(--ink); }
  .back-url .hearth { color: var(--brand-red); }
</style>
</head>
<body>

<section class="card card--front" aria-label="Card front">
  <div class="front-edge front-edge--blue"></div>
  <div class="front-edge front-edge--dark"></div>

  <div class="front-brand">Dale Morrikan<small>Plumbing and Heating</small></div>

  <svg class="contact-panel" width="640" height="366" viewBox="0 0 640 366" aria-hidden="true">
    <path d="M330 0 Q240 183 345 366 L640 366 L640 0 Z" fill="var(--panel)"/>
    <rect x="280" y="98" width="360" height="8" fill="var(--panel-band)"/>
    <rect x="270" y="178" width="370" height="8" fill="var(--panel-band)"/>
    <rect x="280" y="258" width="360" height="8" fill="var(--panel-band)"/>
    <rect x="300" y="334" width="340" height="8" fill="var(--panel-band)"/>
  </svg>

  <div class="name-bar">
    <span class="name">Dale Morrikan</span>
    <span class="role">President</span>
  </div>

  <svg class="hex" style="left:272px;top:39px" viewBox="0 0 34 34" aria-hidden="true">
    <polygon points="17,1 31,9 31,25 17,33 3,25 3,9" fill="var(--white)"/>
    <circle cx="17" cy="13" r="4" fill="var(--blue)"/><path d="M10 24 Q17 15 24 24 Z" fill="var(--blue)"/>
  </svg>
  <svg class="hex" style="left:280px;top:124px" viewBox="0 0 34 34" aria-hidden="true">
    <polygon points="17,1 31,9 31,25 17,33 3,25 3,9" fill="var(--blue)"/>
    <rect x="12" y="8" width="10" height="18" rx="2" fill="none" stroke="var(--white)" stroke-width="2"/>
  </svg>
  <svg class="hex" style="left:272px;top:204px" viewBox="0 0 34 34" aria-hidden="true">
    <polygon points="17,1 31,9 31,25 17,33 3,25 3,9" fill="var(--blue)"/>
    <g fill="none" stroke="var(--white)" stroke-width="1.6"><circle cx="17" cy="17" r="8"/><ellipse cx="17" cy="17" rx="3.5" ry="8"/><line x1="9" y1="17" x2="25" y2="17"/></g>
  </svg>
  <svg class="hex" style="left:292px;top:284px" viewBox="0 0 34 34" aria-hidden="true">
    <polygon points="17,1 31,9 31,25 17,33 3,25 3,9" fill="var(--blue)"/>
    <path d="M8 18 L17 10 L26 18 L23 18 L23 25 L11 25 L11 18 Z" fill="var(--white)"/>
  </svg>

  <div class="contact-row" style="top:124px">P (203) 555-0147<br>C (203) 555-0183</div>
  <div class="contact-row" style="top:200px;left:340px">service@<span class="drain">Drain</span><span class="hearth">Hearth</span>.example<br>www.<span class="drain">Drain</span><span class="hearth">Hearth</span>.example</div>
  <div class="contact-row" style="top:280px;left:360px">275 Larkwell St West,<br>Stamford, Ct 06214</div>
</section>

<section class="card card--back" aria-label="Card back">
  <div class="back-edge back-edge--black-l"></div>
  <div class="back-edge back-edge--deep-l"></div>
  <div class="back-edge back-edge--blue-l"></div>
  <div class="back-edge back-edge--light-r"></div>
  <div class="back-edge back-edge--blue-r"></div>
  <div class="back-edge back-edge--black-r"></div>
  <div class="licence">Fully Licensed and Insured</div>

  <div class="back-content">
    <div class="back-brand">Dale Morrikan<small>Plumbing and Heating</small></div>
    <p class="tagline">Service and repair, remodels, and plumbing in new construction.</p>
    <p class="services">Boilers, Water heaters, Gas lines, Sump pumps,<br>Toilet repairs, Faucet repairs, Pipe thawing,<br>Radiant heating, New construction, Remodels.</p>
    <p class="back-url">WWW.DRAIN<span class="hearth">HEARTH</span>.EXAMPLE</p>
  </div>
</section>

</body>
</html>
```